Wes Hadley Golf Teaching Rack Card

The flyer will be a rack card. Front side only. Nothing on back. 3.75 inches by 8.5 inches. Or close to that. I’d like it to be as colorful as possible and to include several logos in different places.
The brochure is to attract golfers attention and still look traditional and classy not crazy or to artsy. Golf is a very traditional sport and would just like it to look professional and welcoming so golfers no I’m credible in my teaching and they will learn something. I will send a rough idea and a sample of one I had before but use your creative skills and ingenuity to design it. You will have to put my name: Wes Hadley under the NLT logo. It is a requirement by the NLT. Also the logo size must me .0875 inches high. If possible use a gotham or Hoefler text type or something businesslike or similar for my name. Also I am sorry for the different logos available on this file because I am not tech savvy so you will have to choose the best logo and cut it out of the grouping to match what you want to do. I am sorry for all the details. I will be available all weekend if you need more info. or help. I am sure you are very skilled and can tell I am not. Sorry. I laid out a sketch for you so you know what info. verbiage is important. and where to somewhat place the logos. Up to your skill for most of it. Your design! Go for it.!

Target Market(s)

Golfers of all ages from 18-70. Men and Women.

Industry/Entity Type

Golf Industry. Teaching and learning game if golf

Font styles to use
Sans Serif
Other font styles liked:
• Mixture maybe traditional type. Easy to read.

Colors

Designer to choose only greyscale colors for use in the design.

Requirements
Must have
• My JPG golf logo and the NLT official logo. Also will send several other logos to put in. I will tell you where they should go on the rack card.
Nice to have
• Maybe a golf picture from a course with a green and flag as the one on my old brochure I’m sending or similar. It just adds color and eye catching
Should not have
• Nothing hard to read or difficult to comprehend. Pretty straight forward and quality and style in a traditional sense,

```html
<!DOCTYPE html>
<html lang="en">
<head>
<meta charset="utf-8">
<title>Wes Hadley Golf Teaching – Rack Card</title>
<link href="https://fonts.googleapis.com/css2?family=Cinzel:wght@400;600;700&family=Montserrat:wght@400;500;600;700&display=swap" rel="stylesheet">
<style>
  :root{
    --gold:#c89a3c;
    --gold-dark:#b8862c;
    --ink:#1e1e1e;
    --paper:#ffffff;
    --mist:#e7e7ea;
    --band:#231f20;
    --navy:#1f3566;
    --stage:#ececec;
  }
  *{margin:0;padding:0;box-sizing:border-box}
  html,body{width:1139px;height:1200px;overflow:hidden;background:var(--stage)}
  body{position:relative;font-family:"Montserrat",sans-serif;color:var(--ink)}

  .rack-card{position:absolute;left:314px;top:20px;width:510px;height:1160px;background:var(--mist);overflow:hidden;box-shadow:0 4px 18px rgba(0,0,0,.18)}
  .hero-photo{position:absolute;left:0;top:120px;width:510px;height:400px;
    background:linear-gradient(180deg,#cfd3cf 0%,#b9a97a 22%,#8fae4a 42%,#6fa42c 65%,#4f8a1e 100%)}
  .card-shapes{position:absolute;left:0;top:0}

  .brand{position:absolute;left:0;top:46px;width:510px;text-align:center;font-family:"Cinzel",serif;color:var(--gold);font-weight:700;line-height:1.05}
  .brand .brand-name{font-size:34px;letter-spacing:1px}
  .brand .brand-sub{font-size:34px;letter-spacing:1px}

  .tagline{position:absolute;left:20px;top:243px;width:172px;text-align:center;color:#fff;font-weight:600;font-size:23px;letter-spacing:.5px;line-height:30px}
  .tagline .to{display:flex;align-items:center;justify-content:center;gap:14px}
  .tagline .to::before,.tagline .to::after{content:"";width:54px;height:2px;background:#fff}

  .guarantee-seal{position:absolute;left:22px;top:375px;width:110px;height:110px;border-radius:50%;background:var(--gold)}

  .headline{position:absolute;left:0;top:468px;width:510px;text-align:center;font-family:"Cinzel",serif;color:var(--ink)}
  .headline .name{font-size:27px;letter-spacing:1px;line-height:32px}
  .headline .title{font-size:41px;font-weight:600;letter-spacing:1.5px;line-height:46px}

  .package{position:absolute;top:565px;width:235px;height:397px;background:var(--paper);border-radius:9px;text-align:center;box-shadow:0 6px 8px -4px rgba(0,0,0,.2)}
  .package.one{left:13px}
  .package.two{left:265px}
  .package .tab{position:absolute;left:28px;top:-4px;width:180px;height:29px;background:var(--gold);color:#fff;font-weight:600;font-size:15px;line-height:29px;letter-spacing:.5px;clip-path:polygon(0 0,100% 0,96% 100%,4% 100%)}
  .package h3{margin-top:42px;font-family:"Cinzel",serif;font-weight:600;font-size:27px;line-height:29px;letter-spacing:1px}
  .package .price{margin-top:4px;font-weight:700;color:var(--gold);font-size:54px;line-height:58px}
  .package .price sup{font-size:28px;vertical-align:22px;margin-left:2px}
  .package .terms{margin-top:6px;font-size:14px;line-height:18px;letter-spacing:.3px}
  .package .terms sup{font-size:8px}
  .package .includes{display:inline-block;margin-top:6px;width:131px;height:23px;line-height:23px;border-radius:12px;background:var(--gold);color:#fff;font-weight:600;font-size:13px;letter-spacing:.5px}
  .package ul{list-style:none;text-align:left;margin:6px 0 0 13px;font-size:14px;line-height:18.3px;letter-spacing:.3px}
  .package li{padding-left:10px;text-indent:-10px}
  .package li::before{content:"• "}
  .partners{position:absolute;left:0;bottom:10px;width:100%;display:flex;justify-content:center;align-items:baseline;gap:14px;font-weight:700;font-size:17px;line-height:22px;color:var(--gold)}
  .partners .dark{color:var(--ink);font-size:15px}

  .info-tab{position:absolute;left:0;top:987px;width:167px;height:27px;background:var(--paper);border-radius:0 14px 0 0;color:var(--gold);font-size:13px;line-height:27px;padding-left:20px;letter-spacing:.5px}
  .web-band{position:absolute;left:0;top:1014px;width:510px;height:53px;background:var(--band);color:#fff;text-align:center;font-size:25px;line-height:53px;letter-spacing:.5px;padding-right:20px}
  .web-band strong{font-weight:700}
  .footer{position:absolute;left:0;top:1067px;width:510px;height:93px;background:var(--gold);color:#fff}
  .footer .member{position:absolute;left:29px;top:14px;font-size:13px;line-height:16px;letter-spacing:.4px}
  .footer .member strong{display:block;font-size:18px;font-weight:600;line-height:22px;margin-bottom:2px}
  .footer .divider{position:absolute;left:188px;top:14px;width:1px;height:66px;background:#fff}
  .footer .contact{position:absolute;left:210px;top:20px;font-size:13px;line-height:21px;letter-spacing:.4px}
  .member-badge{position:absolute;left:397px;top:1045px;width:100px;height:100px;border-radius:50%;background:var(--navy);border:4px solid #fff;box-shadow:0 0 0 2px var(--navy)}
</style>
</head>
<body>
  <div class="rack-card">
    <div class="hero-photo" role="img" aria-label="Close-up of a golf driver behind a ball on a red tee on a green fairway"></div>

    <svg class="card-shapes" width="510" height="1160" viewBox="0 0 510 1160" aria-hidden="true">
      <path d="M0 150 Q255 264 510 150 V166 Q255 282 0 166 Z" fill="#c89a3c"/>
      <path d="M0 0 H510 V144 Q255 256 0 144 Z" fill="#ffffff"/>
      <path d="M0 156 Q255 270 510 156 V160 Q255 275 0 160 Z" fill="#ffffff"/>
      <path d="M0 510 Q255 395 510 510 V1160 H0 Z" fill="#e7e7ea"/>
      <path d="M0 500 Q255 385 510 500 V512 Q255 398 0 512 Z" fill="#c89a3c"/>
      <path d="M0 492 Q255 378 510 492 V496 Q255 382 0 496 Z" fill="#ffffff"/>
    </svg>

    <div class="brand">
      <div class="brand-name">WES HADLEY</div>
      <div class="brand-sub">GOLF</div>
    </div>

    <div class="tagline">
      <div>BEGINNERS</div>
      <div class="to">TO</div>
      <div>ADVANCES</div>
    </div>

    <div class="guarantee-seal" role="img" aria-label="Money back guarantee seal"></div>

    <div class="headline">
      <div class="name">WES HADLEY</div>
      <div class="title">GOLF TEACHING</div>
    </div>

    <section class="package one">
      <div class="tab">PACKAGE 1</div>
      <h3>GOLF SWING<br>ANALYSIS</h3>
      <div class="price">$59<sup>99</sup></div>
      <p class="terms">I-hour Analysis<br>One Time Limited Offer<br>Reg $79<sup>00</sup></p>
      <div class="includes">INCLUDES:</div>
      <ul>
        <li>Swing Analysis W/Video</li>
        <li>Review Of Swing Technique</li>
        <li>Suggested Tips &amp; Drills</li>
        <li>Video &amp; Sunmary Sent To Your Mobile Devices</li>
      </ul>
      <div class="partners"><span>Swingtrak</span><span class="dark">Launchly</span></div>
    </section>

    <section class="package two">
      <div class="tab">PACKAGE 2</div>
      <h3>SPECIAL<br>GOLF LESSON</h3>
      <div class="price">$225<sup>00</sup></div>
      <p class="terms">LIMITED DEAL<br>3-One Hour Lessons<br>Reg $237<sup>00</sup></p>
      <div class="includes">INCLUDES:</div>
      <ul>
        <li>Video Analysis</li>
        <li>Lesson Summary And</li>
        <li>Tips &amp; Deius</li>
        <li>Action Plan To Improve</li>
        <li>Video Review Sent To Mobile Devices</li>
      </ul>
    </section>

    <div class="info-tab">ADDITIONAL INFO:</div>
    <div class="web-band">www.<strong>whadleygolf</strong>.com</div>

    <footer class="footer">
      <div class="member"><strong>WES HADLEY</strong>CLASS A MEMBEL<br>QTR. CENTURY<br>MEMBER NLT</div>
      <div class="divider"></div>
      <div class="contact">555-014-2387<br>WHADLEYGOLF.NET<br>WHADLEY@NLT.COM</div>
    </footer>
    <div class="member-badge" role="img" aria-label="NLT member badge"></div>
  </div>
</body>
</html>
```